Marketing - Outdoor Vinyl banner, Outdoor Poster, Flyer modifications

Hi, I worked with you in the past and attached flyer designs. It just needs to be tweaked for various prints.
1)Outdoor vinyl banner (4 feet height and 8 feet width) print: Just grand opening pic, logo with name, tagline and call/text us portion.
2)Outdoor Poster (5 feet height and 3 feet width) print: same as above
3) Indoor poster for both horizontal & Vertical prints: Just logo w/ name, tagline, "We are MOVING Next door"
4)Flyer: will give minor modifications to attached flyer designs

```html
<!DOCTYPE html>
<html lang="en">
<head>
<meta charset="utf-8">
<title>Brightway Dental – We Are Moving Next Door</title>
<link href="https://fonts.googleapis.com/css2?family=Roboto+Slab:wght@700;800&display=swap" rel="stylesheet">
<style>
  :root {
    --backdrop: #4a4a4a;
    --navy: #00345a;
    --cyan: #0ab1d9;
    --white: #ffffff;
  }
  * { margin: 0; padding: 0; box-sizing: border-box; }
  html, body {
    width: 1096px;
    height: 1200px;
    overflow: hidden;
    background: var(--backdrop);
  }
  .sign {
    position: absolute;
    left: 40px;
    top: 272px;
    width: 1016px;
    height: 656px;
    font-family: "Roboto Slab", Georgia, serif;
    font-weight: 700;
    text-align: center;
  }
  .sign__header {
    height: 190px;
    background: var(--navy);
    display: flex;
    align-items: center;
    justify-content: center;
    gap: 20px;
  }
  .brand__dot {
    width: 44px;
    height: 44px;
    border-radius: 50%;
    background: var(--cyan);
  }
  .brand__name {
    color: var(--cyan);
    font-size: 50px;
    letter-spacing: 1px;
    line-height: 1;
  }
  .sign__message {
    height: 346px;
    background: var(--cyan);
    color: var(--white);
    display: flex;
    flex-direction: column;
    align-items: center;
    justify-content: center;
    padding-top: 4px;
  }
  .message__lead {
    font-size: 56px;
    line-height: 1;
    margin-bottom: 40px;
  }
  .message__main {
    font-size: 122px;
    font-weight: 800;
    line-height: 1;
  }
  .sign__footer {
    height: 120px;
    background: var(--navy);
    color: var(--cyan);
    display: flex;
    align-items: center;
    justify-content: center;
    font-size: 46px;
    line-height: 1;
  }
</style>
</head>
<body>
  <section class="sign">
    <header class="sign__header">
      <span class="brand__dot"></span>
      <span class="brand__name">Brightway Dental</span>
    </header>
    <div class="sign__message">
      <p class="message__lead">WE ARE MOVING</p>
      <p class="message__main">NEXT DOOR!</p>
    </div>
    <footer class="sign__footer">
      <p>EXCITED TO FIND HOME!</p>
    </footer>
  </section>
</body>
</html>
```